Training company needs a Quick Reference Card design

We have draft skeleton of the design and most of the text. But we need a designer to take it the rest if the way.
I have designed a 2 page quick reference card - it is meant to be a 2-sided document. The first page is portrait, the back page can either be portrait or landscape, I'm not too concerned, whichever fits best.
Section called 'Maps' on front, a map is a collection of documents (like a manual), a topic is a document (like a page or section of a manual) and a block is a section of a document. The graphic is mean to illustrate the hierarchy but essentially a map is a big document with smaller documents in it.
Please use the company's logo colors to differentiate the different sections with minimal/ highlight only use of the darkest color, preferably.
Please use the icons for the corresponding Information types in the chart of the back - except please re-design the icons color scheme to match the company's logo/website colors.

Target Market(s)

Technical writers, after attending our training course, as an ongoing resource for them

Industry/Entity Type

It Company

Font styles to use
Sans Serif

Requirements
Must have
• Must adhere to look and feel of brand/ website. www.lumarockwise.com
Nice to have
• Please keep the design modern and slick looking, not too busy, easy to read

```html
<!DOCTYPE html>
<html lang="en">
<head>
<meta charset="utf-8">
<title>Quick Reference Card</title>
<link href="https://fonts.googleapis.com/css2?family=Arimo:wght@400;700&family=Nunito:wght@800;900&display=swap" rel="stylesheet">
<style>
:root{
  --frame:#3d3d3f;
  --navy:#221c8e;
  --blue:#1d5fcc;
  --blue-mid:#2f86e0;
  --cyan:#19a3dc;
  --sky:#e8f5fb;
  --line:#3a33b4;
  --ink:#1e1e1e;
  --white:#ffffff;
}
*{box-sizing:border-box;margin:0;padding:0}
html,body{width:1200px;height:2179px;overflow:hidden}
body{background:var(--frame);font-family:"Arimo",Arial,sans-serif;color:var(--ink);position:relative}
.abs{position:absolute}

/* front page */
.front{left:169px;top:52px;width:862px;height:1118px;
  background:linear-gradient(180deg,#2a5fd6 0%,#1f4fc4 40%,#2a73dc 85%,#3a8ae6 100%);overflow:hidden}
.front::before{content:"";position:absolute;left:0;right:0;top:137px;height:90px;
  background:linear-gradient(90deg,rgba(255,255,255,.06),rgba(255,255,255,.18),rgba(255,255,255,.04))}
.front::after{content:"";position:absolute;left:0;right:0;bottom:0;height:110px;
  background:linear-gradient(90deg,rgba(255,255,255,.05),rgba(255,255,255,.2),rgba(255,255,255,.05))}
.front-header{left:0;top:0;width:862px;height:137px;
  background:linear-gradient(180deg,#ffffff 0%,#ffffff 80%,#dfe8f8 100%);border-bottom:4px solid #8fb0ec}
.brand{left:24px;top:42px;display:flex;align-items:center;gap:10px}
.brand-dot{width:52px;height:52px;border-radius:50%;background:var(--navy)}
.brand-name{font-family:"Arimo",Arial,sans-serif;font-weight:700;font-size:22px;color:var(--navy);letter-spacing:.3px}
.card-title{right:52px;top:44px;font-family:"Nunito",Arial,sans-serif;font-weight:900;font-size:47px;color:var(--navy)}

.panel{background:var(--sky);border:2px solid #9fd2ee;border-radius:12px;overflow:hidden}
.panel-bar{height:42px;background:linear-gradient(180deg,#1f55c8,#3b8fe6);color:var(--white);
  font-weight:700;font-size:22px;text-align:center;line-height:42px}
.topic-label{font-weight:700;font-size:23px;color:var(--navy);text-align:center;width:151px}
.topic-card{width:151px;height:142px;border-radius:12px;background:linear-gradient(180deg,#15a2dc,#1b8fd1)}
.pill{left:13px;width:125px;height:30px;border-radius:15px;background:var(--white);
  font-size:15px;text-align:center;line-height:30px;color:var(--ink)}

.note{background:var(--white);border:2px solid #7c86e6;border-radius:6px;padding:9px 12px;
  font-size:16px;line-height:20px}
.note b{color:var(--navy)}
.cell{background:var(--white);border:2px solid var(--line);border-radius:6px;padding:8px 10px;
  font-size:15.5px;line-height:19.5px}
.cell h3{font-size:15.5px;font-weight:400;color:var(--navy);margin-bottom:6px}
.cell ol{padding-left:20px}

/* back page */
.back{left:46px;top:1257px;width:1110px;height:865px;background:var(--white);overflow:hidden}
.back-band{left:0;top:0;width:1110px;height:72px;
  background:linear-gradient(90deg,#6fb1ea 0%,#2f6fd6 45%,#1c4ec4 100%)}
.back-band::after{content:"";position:absolute;left:0;right:0;bottom:0;height:20px;
  background:linear-gradient(180deg,rgba(255,255,255,0),#ffffff)}
.hex{left:1046px;top:20px}

.grid{left:64px;top:80px;width:991px;border-collapse:separate;border-spacing:0;
  border:2px solid var(--line);border-radius:10px;overflow:hidden;table-layout:fixed}
.grid th,.grid td{border-right:1px solid #8f93d8;border-bottom:1px solid #8f93d8;vertical-align:top}
.grid tr > :last-child{border-right:none}
.grid tr:last-child > *{border-bottom:none}
.grid thead th{height:66px;background:linear-gradient(180deg,#1d49c1,#3a8fe6);color:var(--white);
  font-size:23px;font-weight:700;vertical-align:bottom;padding-bottom:6px;border-right:1px solid #6f8fe0}
.grid tbody th{color:var(--navy);font-size:19px;line-height:23px;font-weight:700;text-align:center;vertical-align:middle}
.grid tbody td{font-size:14px;line-height:17px;padding:8px 12px;color:#333}
.icon{top:52px;width:50px;height:50px}
</style>
</head>
<body>

<section class="abs front" aria-label="Quick reference card, front">
  <header class="abs front-header">
    <div class="abs brand"><span class="brand-dot"></span><span class="brand-name">LUMAROCKWISE.com</span></div>
    <h1 class="abs card-title">Quick Reference Card</h1>
  </header>

  <div class="abs panel" style="left:37px;top:175px;width:368px;height:252px">
    <div class="panel-bar">Map</div>
  </div>
  <div class="abs topic-label" style="left:61px;top:224px">Topic</div>
  <div class="abs topic-label" style="left:228px;top:224px">Topic</div>
  <div class="abs topic-card" style="left:61px;top:265px">
    <div class="abs pill" style="top:27px">Primary Block</div>
    <div class="abs pill" style="top:80px">Sub-Block</div>
  </div>
  <div class="abs topic-card" style="left:228px;top:265px">
    <div class="abs pill" style="top:27px">Primary Block</div>
    <div class="abs pill" style="top:80px">Sub-Block</div>
  </div>

  <p class="abs note" style="left:415px;top:175px;width:410px;height:80px"><b>A map</b> is a file that organizes topics into structured collections of information. Maps specify hierarchy and relationships among topics.</p>
  <p class="abs note" style="left:415px;top:265px;width:410px;height:75px"><b>A topic</b> is a group of related blocks with a title. Use the chunking principle to group together relevant blocks.</p>
  <p class="abs note" style="left:415px;top:350px;width:410px;height:77px"><b>A block</b> is a bite-sized chunk of information about one main idea that allows the writer to organize the material into logical sections.</p>

  <div class="abs panel" style="left:37px;top:446px;width:788px;height:217px">
    <div class="panel-bar">General writing rules</div>
  </div>
  <div class="abs cell" style="left:50px;top:500px;width:249px;height:154px">
    <h3>Effective sentences</h3>One main agent, action &amp; outcome. Use active voice and simplest tense possible. No more than 7 sentences per paragraph. Use lists and tables.</div>
  <div class="abs cell" style="left:308px;top:500px;width:246px;height:154px">
    <h3>Special characters</h3>Avoid special characters, spell out words instead. Remove parentheses, colons and dashes. Avoid using quotation marks and slashes.</div>
  <div class="abs cell" style="left:565px;top:500px;width:248px;height:154px">
    <h3>Plain language</h3>Write in short sentences. Provide useful titles. Use clear familiar words. Avoid excess words. Be consistent.</div>

  <div class="abs cell" style="left:37px;top:682px;width:388px;height:119px">
    <h3>3 Questions to ask before you start writing:</h3>
    <ol><li>What is the purpose of this information?</li><li>What is the desired user response of this information?</li><li>Who is the audience?</li></ol></div>
  <div class="abs cell" style="left:435px;top:682px;width:390px;height:119px">
    <h3>2 Types of language arts:</h3>LAFI – Language arts for information<br>LAFPR – language arts for personal response</div>

  <div class="abs panel" style="left:37px;top:818px;width:788px;height:260px">
    <div class="panel-bar">4 Cognitive Principles</div>
  </div>
  <div class="abs cell" style="left:50px;top:872px;width:183px;height:184px">
    <h3>Consistency</h3>Use similar terms and structures. Pick a term and stick with it. Use the same sequence of blocks. Use consistent styles.</div>
  <div class="abs cell" style="left:244px;top:872px;width:183px;height:184px">
    <h3>Chunking</h3>Maximum of nine (7 +/- 2) items in a list, rows in a table, blocks in a topic, or topics in a map.</div>
  <div class="abs cell" style="left:437px;top:872px;width:183px;height:184px">
    <h3>Relevance</h3>Group similar items together. Separate relevance? Separate block. Irrelevant? Delete it.</div>
  <div class="abs cell" style="left:629px;top:872px;width:184px;height:184px">
    <h3>Titling</h3>Name everything. Name every block, every topic, every map and every table column.</div>
</section>

<section class="abs back" aria-label="Quick reference card, back">
  <div class="abs back-band"></div>
  <svg class="abs hex" width="74" height="66" viewBox="0 0 74 66"><polygon points="0,0 74,0 74,44 37,66 0,44" fill="#1c4ec4"/></svg>

  <table class="abs grid">
    <colgroup><col style="width:121px"><col style="width:174px"><col style="width:170px"><col style="width:179px"><col style="width:174px"><col style="width:173px"></colgroup>
    <thead><tr><th></th><th>Reference</th><th>Concept</th><th>Principle</th><th>Process</th><th>Task</th></tr></thead>
    <tbody>
      <tr style="height:93px"><th>Definition</th><td>Describes things the reader needs to know</td><td>Explains things the reader needs to understand</td><td>Advises the read-er what they need to do or not do and when</td><td>Demonstrates to the reader how things work</td><td>Instructs the reader on how to do things</td></tr>
      <tr style="height:128px"><th>Types of authoring models</th><td>Sentenc-es/phrases<br>Lists (ol, ul)<br>Tables<br>Diagrams<br>Part-description<br>Part-function</td><td>Sentenc-es/phrases<br>Lists (ol, ul)<br>Tables<br>Illustrations</td><td>Sentenc-es/phrases<br>Lists (ol, ul)<br>Tables<br>Decision tree<br>Graphic</td><td>Sentenc-es/phrases<br>Stage ordered list<br>When/then condition tree<br>Graphic example</td><td>Sentenc-es/phrases<br>Lists<br>If/then decision tree<br>Graphic example</td></tr>
      <tr style="height:160px"><th>Titling best practices</th><td>Describes the item and anything that differentiates it from other items</td><td>Use the plural form of the noun, if one exists. Don’t add addi-tional words such as “About”, “What is”, or “Definition”</td><td>Identifies the principle and ex-presses the gravi-ty of the principle. Formula= gravity + principle, or prin-ciple + gravity</td><td>Human processes: Gerund of verb + noun “Grooming a dog”.<br>System processes: Use “How (item) works” Ex “How engines work”</td><td>Starts with an im-perative verb, do not use gerund. “Mow the lawn” “Boil and egg” “Register for a course”</td></tr>
      <tr style="height:63px"><th>Primary block title</th><td style="vertical-align:middle">Introduction</td><td style="vertical-align:middle">Definition</td><td style="vertical-align:middle">Statement</td><td style="vertical-align:middle">Summary</td><td style="vertical-align:middle">Purpose</td></tr>
      <tr style="height:114px"><th>Primary block content</th><td>Provide a descrip-tion of the refer-ence topic and how it would be used</td><td>Provide the exact meaning of the concept</td><td>Provide a high-level summary of the principle</td><td>Provide a short explanation of the purpose of the process, or the need for the pro-cess</td><td>Provide an explanation of why or when the reader would use the task</td></tr>
      <tr style="height:128px"><th>Tips and examples</th><td></td><td></td><td></td><td></td><td></td></tr>
    </tbody>
  </table>

  <svg class="abs icon" style="left:247px" viewBox="0 0 50 50" aria-hidden="true"><circle cx="25" cy="25" r="22" fill="#fff" stroke="#221c8e" stroke-width="3"/><circle cx="25" cy="14" r="3.5" fill="#221c8e"/><rect x="21.5" y="20" width="7" height="18" rx="1.5" fill="#221c8e"/></svg>
  <svg class="abs icon" style="left:419px" viewBox="0 0 50 50" aria-hidden="true"><circle cx="25" cy="25" r="22" fill="#fff" stroke="#221c8e" stroke-width="3"/><path d="M25 10a10 10 0 0 0-6 18v5h12v-5a10 10 0 0 0-6-18z" fill="none" stroke="#221c8e" stroke-width="2.5"/><path d="M27 14l-5 8h5l-3 7" fill="none" stroke="#f2a21b" stroke-width="2.5"/><path d="M20 37h10" stroke="#221c8e" stroke-width="2.5"/></svg>
  <svg class="abs icon" style="left:594px" viewBox="0 0 50 50" aria-hidden="true"><circle cx="25" cy="25" r="22" fill="#fff" stroke="#221c8e" stroke-width="3"/><path d="M17 27V16a2 2 0 0 1 4 0v8V12a2 2 0 0 1 4 0v12V13a2 2 0 0 1 4 0v11v-8a2 2 0 0 1 4 0v14c0 6-4 9-8 9s-7-3-9-7l-3-5a2 2 0 0 1 3-2z" fill="none" stroke="#221c8e" stroke-width="2.2" stroke-linejoin="round"/></svg>
  <svg class="abs icon" style="left:766px" viewBox="0 0 50 50" aria-hidden="true"><circle cx="25" cy="25" r="22" fill="#fff" stroke="#221c8e" stroke-width="3"/><circle cx="21" cy="27" r="8" fill="none" stroke="#221c8e" stroke-width="4" stroke-dasharray="3 2.3"/><circle cx="21" cy="27" r="3" fill="#f2a21b"/><circle cx="32" cy="17" r="5" fill="none" stroke="#221c8e" stroke-width="3" stroke-dasharray="2 1.9"/><circle cx="32" cy="17" r="1.8" fill="#f2a21b"/></svg>
  <svg class="abs icon" style="left:939px" viewBox="0 0 50 50" aria-hidden="true"><circle cx="25" cy="25" r="22" fill="#fff" stroke="#221c8e" stroke-width="3"/><rect x="15" y="12" width="20" height="26" rx="2" fill="none" stroke="#221c8e" stroke-width="2.5"/><rect x="20" y="9" width="10" height="5" rx="1" fill="#221c8e"/><path d="M19 26l5 5 9-12" fill="none" stroke="#f2a21b" stroke-width="3" stroke-linecap="round"/></svg>
</section>

</body>
</html>
```